Healthcare website - Diabetic Shoes - Elderfund - No Cost

I am looking to upgrade my website. I do not want to use Wordpress, Adobe Muse or another designing program. The code should be easily editable using textpad or VI. After the project is done I want to easily add my custom PHP code.

Features
Creative and Modern Design .
Fully responsive site for use on mobile devices
bootstrap, jquery

My current website is
www.pebblewalkco.com

Target Market(s)

Older people who have diabetes. Target market is +60 years old, but we do have younger people going to the site to help out their parents.

Industry/Entity Type

Healthcare

Coding

Coded - Design and coding required

Number of Pages Required

2 page

Colors

Designer to choose colors to be used in the design.

Requirements
Must have
• The code should be easily editable using textpad or VI. After the project is done I want to easily add my custom PHP code.
• The first page will be the home page and the other page I need is this form.
• https://www.pebblewalkco.com/pebble-walk-co-do-i-qualify.php
Should not have
• I do not want to use Wordpress, Adobe Muse or another designing program.

```html
<!DOCTYPE html>
<html lang="en">
<head>
<meta charset="utf-8">
<title>Pebble Walk Co Do I Qualify?</title>
<link rel="stylesheet" href="https://fonts.googleapis.com/css2?family=Open+Sans:wght@400;600;700&display=swap">
<style>
:root{
  --steel:#547ea4;
  --steel-dark:#4a7398;
  --ink:#333a40;
  --heading:#4b4f54;
  --text:#4a4a4a;
  --line:#c9c9c9;
  --field-border:#9a9a9a;
  --footer:#14141c;
  --white:#ffffff;
}
*{box-sizing:border-box;margin:0;padding:0}
html,body{width:1200px;height:2474px;overflow:hidden;background:var(--white)}
body{font-family:"Open Sans",Arial,sans-serif;color:var(--text)}
.page{position:relative;width:1200px;height:2474px}
.abs{position:absolute}

/* top bar */
.topbar{left:0;top:0;width:1200px;height:41px;background:var(--steel);color:var(--white);font-size:10px}
.topbar .contact{position:absolute;left:822px;top:14px;display:flex;align-items:center;gap:6px}
.topbar .sep{position:absolute;top:10px;width:1px;height:21px;background:rgba(255,255,255,.7)}
.topbar .social{position:absolute;top:10px;display:flex;gap:6px}
.topbar .login{position:absolute;left:1085px;top:14px;display:flex;align-items:center;gap:5px}

/* header */
.brand{left:62px;top:62px;font-size:32px;font-weight:600;color:var(--steel);letter-spacing:.5px}
.nav{left:478px;top:79px;display:flex;gap:21px;font-size:11px;color:var(--ink);text-transform:uppercase}
.header-rule{left:59px;top:131px;width:1086px;height:1px;background:var(--line)}

/* intro */
.intro{left:62px;top:158px;width:1080px}
.intro h1{font-size:33px;font-weight:700;color:var(--ink);margin-bottom:14px}
.intro p{font-size:14.5px;line-height:23px;color:var(--text);margin-bottom:39px}
.intro-rule{left:59px;top:414px;width:1086px;height:1px;background:var(--line)}

/* section headings */
.section-title{left:0;width:1200px;text-align:center;color:var(--heading);font-weight:700;font-size:34px;line-height:40px}
.section-title small{display:block;font-size:24px;line-height:32px}
.bar{left:562px;width:77px;height:5px;background:var(--steel)}

/* fields */
.fields{display:grid;grid-template-columns:316px 316px;column-gap:55px;row-gap:13px}
.fields.single{grid-template-columns:316px}
.field label{display:block;font-size:11.5px;font-weight:600;color:#222;line-height:12px;margin-bottom:0}
.field .input{height:27px;border:1px solid var(--field-border);border-radius:3px;background:var(--white)}
.field .select{position:relative;font-size:10px;color:#777;padding:6px 8px}
.field .select svg{position:absolute;right:10px;top:11px}

/* products */
.products{left:291px;top:1640px;display:grid;grid-template-columns:253px 252px 200px;row-gap:11px}
.check{display:flex;align-items:center;gap:7px;font-size:15px;color:#555}
.check .box{width:16px;height:16px;border:1px solid #a5a5a5;border-radius:2px}

/* confirm */
.comments{left:257px;top:1863px}
.comments .input{width:665px;height:118px}
.consent{left:259px;top:2011px;width:670px;font-size:12px;line-height:14px;color:#555}
.submit{left:503px;top:2094px;width:194px;height:35px;background:var(--steel);color:var(--white);font-size:17px;font-weight:600;display:flex;align-items:center;justify-content:center;border-radius:2px}

/* footer */
.footer{left:0;top:2191px;width:1200px;height:283px;background:var(--footer);color:var(--white)}
.footer .brand-foot{position:absolute;left:89px;top:40px;font-size:32px;font-weight:600;color:#b9bcc2;letter-spacing:.5px}
.footer .phone{position:absolute;left:89px;top:114px;display:flex;align-items:center;gap:14px;font-size:20px}
.footer .follow{position:absolute;left:89px;top:156px;font-size:19px}
.footer .social{position:absolute;left:89px;top:205px;display:flex;gap:12px}
.footer .links{position:absolute;left:512px;top:62px;list-style:none;font-size:13px;line-height:24.4px;text-transform:uppercase}
.footer .catalog{position:absolute;left:868px;top:57px;width:220px;font-size:18px;font-weight:700;line-height:23px;text-transform:uppercase}
.footer .catalog-btn{position:absolute;left:868px;top:152px;width:194px;height:35px;background:var(--steel-dark);font-size:18px;font-weight:600;display:flex;align-items:center;justify-content:center;border-radius:2px}
.footer .foot-rule{position:absolute;left:303px;top:263px;width:589px;height:1px;background:#3a3a44}
.footer .copy{position:absolute;left:0;width:1200px;top:266px;text-align:center;font-size:7px;color:#77787e}
</style>
</head>
<body>
<div class="page">

  <div class="abs topbar">
    <div class="contact">
      <svg width="10" height="10" viewBox="0 0 24 24" aria-hidden="true"><path fill="#fff" d="M6.6 10.8a15 15 0 0 0 6.6 6.6l2.2-2.2c.3-.3.7-.4 1-.2 1.1.4 2.3.6 3.6.6.6 0 1 .4 1 1V20c0 .6-.4 1-1 1C10.6 21 3 13.4 3 4c0-.6.4-1 1-1h3.5c.6 0 1 .4 1 1 0 1.3.2 2.5.6 3.6.1.3 0 .7-.2 1z"/></svg>
      <span>1-800-555-0142 &nbsp;Call Us!</span>
    </div>
    <div class="sep" style="left:973px"></div>
    <div class="social" style="left:988px">
      <svg width="21" height="21" aria-hidden="true"><circle cx="10.5" cy="10.5" r="9.5" fill="none" stroke="#fff" stroke-width="1.4"/></svg>
      <svg width="21" height="21" aria-hidden="true"><circle cx="10.5" cy="10.5" r="9.5" fill="none" stroke="#fff" stroke-width="1.4"/></svg>
    </div>
    <div class="sep" style="left:1056px"></div>
    <div class="login">
      <svg width="11" height="11" viewBox="0 0 24 24" aria-hidden="true"><circle cx="12" cy="12" r="11" fill="#fff"/><circle cx="12" cy="9" r="4" fill="#547ea4"/><path d="M5 19c2-4 12-4 14 0" fill="#547ea4"/></svg>
      <span>LOGIN</span>
    </div>
  </div>

  <div class="abs brand">Pebble Walk Co</div>
  <nav class="abs nav">
    <span>Home</span><span>Pebble Walk Co! Do I Qualify!</span><span>Why Diabetic Shoes?</span><span>Shoes</span><span>Products</span><span>Shoe Fitter Jobs</span><span>FAQ</span>
  </nav>
  <div class="abs header-rule"></div>

  <section class="abs intro">
    <h1>Pebble Walk Co Do I Qualify?</h1>
    <p>You may be eligible for shoes - at no cost to you! Enter your information in the form below to find out if you qualify for shoe coverage. Elderfund or your insurance provider may cover the cost of one pair of shoes and three pairs of custom or heat molded insoles per calendar year. Find out if you qualify now!</p>
    <p>Besides Elderfund, here is a list of private insurance providers: Silverline Senior Health, Northgate Health, Meridian Shield, VetCare Plus, Crestway, Hudson Shield, Lumina Health, Bluebay Health Plan, Care Forward, Summit Life, Safe Harbor Plans, Unity Health Care, TriState Care, Wellspring. Any many more.</p>
  </section>
  <div class="abs intro-rule"></div>

  <!-- Personal information -->
  <h2 class="abs section-title" style="top:440px">Personal Information</h2>
  <div class="abs bar" style="top:491px"></div>
  <div class="abs fields" style="left:257px;top:511px">
    <div class="field"><label>First Name:</label><div class="input"></div></div>
    <div class="field"><label>Last Name:</label><div class="input"></div></div>
    <div class="field"><label>Address:</label><div class="input"></div></div>
    <div class="field"><label>City:</label><div class="input"></div></div>
    <div class="field"><label>State:</label><div class="input"></div></div>
    <div class="field"><label>Zip:</label><div class="input"></div></div>
    <div class="field"><label>Gender:</label><div class="input"></div></div>
    <div class="field"><label>Date of Birth:</label><div class="input"></div></div>
    <div class="field"><label>Email:</label><div class="input"></div></div>
    <div class="field"><label>Phone number:</label><div class="input"></div></div>
  </div>

  <!-- Elderfund -->
  <h2 class="abs section-title" style="top:797px">Elderfund and Insurance Information</h2>
  <div class="abs bar" style="top:852px"></div>
  <div class="abs fields" style="left:257px;top:871px">
    <div class="field"><label>Is Elderfund Your Primary Insurance?</label>
      <div class="input select">Yes<svg width="8" height="5" aria-hidden="true"><path d="M0 0h8L4 5z" fill="#333"/></svg></div></div>
    <div class="field"><label>Elderfund#:</label><div class="input"></div></div>
  </div>

  <!-- Supplementary -->
  <h2 class="abs section-title" style="top:934px">Supplementary/Secondary Insurance Information</h2>
  <div class="abs bar" style="top:989px"></div>
  <div class="abs fields single" style="left:443px;top:1008px;row-gap:16px">
    <div class="field"><label>Name of Insurance Company:</label><div class="input"></div></div>
    <div class="field"><label>Insurance Phone #:</label><div class="input"></div></div>
    <div class="field"><label>Policy Number / Member Id:</label><div class="input"></div></div>
  </div>

  <!-- Physician -->
  <h2 class="abs section-title" style="top:1180px">Primary Physician Information<small>(M.D or D.O only No Podiatrist Please)</small></h2>
  <div class="abs bar" style="top:1268px"></div>
  <div class="abs fields" style="left:257px;top:1290px">
    <div class="field"><label>First Name:</label><div class="input"></div></div>
    <div class="field"><label>Last Name:</label><div class="input"></div></div>
    <div class="field"><label>Address:</label><div class="input"></div></div>
    <div class="field"><label>City:</label><div class="input"></div></div>
    <div class="field"><label>State:</label><div class="input"></div></div>
    <div class="field"><label>Zip:</label><div class="input"></div></div>
    <div class="field"><label>Phone:</label><div class="input"></div></div>
    <div class="field"><label>Fax:</label><div class="input"></div></div>
  </div>

  <!-- Products -->
  <h2 class="abs section-title" style="top:1527px">Elderfund Covered Products<small>(Check next to each product you want to receive)</small></h2>
  <div class="abs bar" style="top:1613px"></div>
  <div class="abs products">
    <div class="check"><span class="box"></span>Tens Unit</div>
    <div class="check"><span class="box"></span>Seat Lift</div>
    <div class="check"><span class="box"></span>Back Brace</div>
    <div class="check"><span class="box"></span>Ankle Brace</div>
    <div class="check"><span class="box"></span>Knee Brace</div>
    <div class="check"><span class="box"></span>Wrist Brace</div>
    <div class="check"><span class="box"></span>Compounded Cream</div>
  </div>

  <!-- Confirm -->
  <h2 class="abs section-title" style="top:1772px">Confirm &amp; Submit Application</h2>
  <div class="abs bar" style="top:1828px"></div>
  <div class="abs field comments"><label>Additional Comments:</label><div class="input"></div></div>
  <p class="abs consent">By submitting this information, I authorize PebbleWalkCo.com/Harborline Medical Supply Inc., its affiliates, subsidiaries, or parent company to contact me by phone or email. Please be assured that we value and protect your privacy. Remember, there is no purchase necessary to see if you qualify.</p>
  <div class="abs submit">Submit</div>

  <footer class="abs footer">
    <div class="brand-foot">Pebble Walk Co</div>
    <div class="phone">
      <svg width="16" height="16" viewBox="0 0 24 24" aria-hidden="true"><path fill="#547ea4" d="M6.6 10.8a15 15 0 0 0 6.6 6.6l2.2-2.2c.3-.3.7-.4 1-.2 1.1.4 2.3.6 3.6.6.6 0 1 .4 1 1V20c0 .6-.4 1-1 1C10.6 21 3 13.4 3 4c0-.6.4-1 1-1h3.5c.6 0 1 .4 1 1 0 1.3.2 2.5.6 3.6.1.3 0 .7-.2 1z"/></svg>
      <span>1-800-555-0142 &nbsp;Call Us!</span>
    </div>
    <div class="follow">Follow Us:</div>
    <div class="social">
      <svg width="34" height="34" aria-hidden="true"><circle cx="17" cy="17" r="15.5" fill="none" stroke="#5e88ad" stroke-width="2"/></svg>
      <svg width="34" height="34" aria-hidden="true"><circle cx="17" cy="17" r="15.5" fill="none" stroke="#5e88ad" stroke-width="2"/></svg>
    </div>
    <ul class="links">
      <li>Home</li><li>Pebble Walk Co! Do I Qualify!</li><li>Why Diabetic Shoes?</li><li>Shoes</li><li>Products</li><li>Shoe Fitter Jobs</li><li>FAQ</li>
    </ul>
    <div class="catalog">Request a Free Diabetic Shoe Catalog</div>
    <div class="catalog-btn">Request Catalog</div>
    <div class="foot-rule"></div>
    <div class="copy">© All rights reserved.</div>
  </footer>

</div>
</body>
</html>
```